Business card design for a debt inventory management software company

We need a business card design to help us move into the next phase of our business. We developed an innovative solution to help companies collect their bad debts. We are moving into a new era and branching out into new industries. We are open to design ideas but would like that they have a similar feel/look to our website and include our logo. https://www.ledgorvia.com

Target Market(s)

Finance Industry, Telecom Industry, Utility Industry, Healthcare Industry, Insurance Industry

Industry/Entity Type

Software

Contact Information for Business Card

Include Name, Title, Phone, Email, website, address, and logo

Font styles to use
Sans Serif

Colors

Designer to choose colors to be used in the design.

Requirements
Must have
• A similar look and feel to our website. https://www.ledgorvia.com

```html
<!DOCTYPE html>
<html lang="en">
<head>
<meta charset="utf-8">
<title>Ledgorvia Software – Business Card</title>
<link rel="stylesheet" href="https://fonts.googleapis.com/css2?family=Raleway:wght@400&family=Lato:wght@400;700&family=Open+Sans:wght@400&display=swap">
<style>
  :root {
    --backdrop: #4b4b4b;
    --card-white: #ffffff;
    --navy: #25307e;
    --ink: #555555;
    --rule: #9a9a9a;
    --green: #8cbd3a;
    --maroon: #9b1b1f;
    --red: #e31e24;
    --yellow: #f2b417;
    --olive: #9c8434;
    --blue: #283a8c;
  }
  * { margin: 0; padding: 0; box-sizing: border-box; }
  html, body { width: 1200px; height: 802px; overflow: hidden; background: var(--backdrop); }
  .canvas { position: relative; width: 1200px; height: 802px; }

  .card {
    position: absolute; top: 274px; width: 443px; height: 265px;
    box-shadow: 3px 4px 8px rgba(0,0,0,0.45);
    overflow: hidden;
  }
  .card--front { left: 136px; background: var(--card-white); }
  .card--back {
    left: 624px;
    background: linear-gradient(to bottom,
      var(--blue) 0%, #c8a51c 14%, var(--yellow) 30%, #f08a1a 40%,
      var(--red) 58%, #a8141a 75%, #b43a1e 84%, var(--green) 100%);
  }

  .brand {
    position: absolute; right: 29px; top: 62px;
    display: flex; align-items: center; gap: 10px;
    font-family: "Raleway", sans-serif; font-size: 26px; color: var(--navy);
    white-space: nowrap;
  }
  .brand__mark { width: 26px; height: 26px; background: var(--navy); border-radius: 50%; }

  .person { position: absolute; left: 27px; top: 138px; right: 29px; }
  .person__name { font-family: "Lato", sans-serif; font-size: 19px; color: var(--navy); font-weight: 400; line-height: 1.1; }
  .person__name b { font-weight: 700; }
  .person__title-row { display: flex; align-items: center; gap: 6px; margin-top: 1px; }
  .person__title { font-family: "Open Sans", sans-serif; font-size: 12.5px; color: var(--ink); white-space: nowrap; }
  .person__rule { flex: 1; height: 1px; background: var(--rule); }

  .contact { position: absolute; left: 26px; top: 187px; list-style: none;
    font-family: "Open Sans", sans-serif; font-size: 13px; color: var(--ink); line-height: 16px; }
  .contact li { display: flex; align-items: center; gap: 6px; }
  .contact svg { width: 10px; height: 10px; fill: var(--navy); }

  .address { position: absolute; right: 29px; top: 204px; text-align: right;
    font-family: "Open Sans", sans-serif; font-size: 13px; color: var(--ink); line-height: 16px; }

  .color-bar { position: absolute; left: 0; right: 0; bottom: 0; height: 11px; display: flex; }
  .color-bar span { flex: 1; }
  .color-bar span:nth-child(1) { background: var(--green); }
  .color-bar span:nth-child(2) { background: var(--maroon); }
  .color-bar span:nth-child(3) { background: var(--red); }
  .color-bar span:nth-child(4) { background: var(--yellow); }
  .color-bar span:nth-child(5) { background: var(--olive); }
  .color-bar span:nth-child(6) { background: var(--blue); }

  .back__name {
    position: absolute; left: 0; right: 0; top: 112px; text-align: center;
    font-family: "Raleway", sans-serif; font-size: 33px; color: #ffffff; white-space: nowrap;
  }
</style>
</head>
<body>
<main class="canvas">
  <section class="card card--front" aria-label="Card front">
    <div class="brand"><span class="brand__mark"></span>Ledgorvia Software</div>

    <div class="person">
      <p class="person__name"><b>Marcus</b> Hale</p>
      <div class="person__title-row">
        <span class="person__title">Managing Director</span>
        <span class="person__rule"></span>
      </div>
    </div>

    <ul class="contact">
      <li><svg viewBox="0 0 10 10"><path d="M0 3.5C0 2 2 1 5 1s5 1 5 2.5v1H7.5V3.2h-5v1.3H0z"/><rect x="1.5" y="5" width="7" height="4" rx="1"/></svg>330.555.0142</li>
      <li><svg viewBox="0 0 10 10"><rect x="2.5" y="0.5" width="5" height="3"/><rect x="0" y="3.5" width="10" height="4" rx="1"/><rect x="2.5" y="6.5" width="5" height="3"/></svg>330.555.0187</li>
      <li><svg viewBox="0 0 10 10"><path d="M0 2h10v6H0z M1 2.8l4 3 4-3" /></svg>info@ledgorvia.com</li>
    </ul>

    <address class="address" style="font-style:normal">
      248 Carrow Ridge Avenue<br>
      Suite 310, Brookhaven, Ohio 44190
    </address>

    <div class="color-bar"><span></span><span></span><span></span><span></span><span></span><span></span></div>
  </section>

  <section class="card card--back" aria-label="Card back">
    <p class="back__name">Ledgorvia Software</p>
  </section>
</main>
</body>
</html>
```